Nine Rung Ledger Remedy Seminar

I would like a flyer to hand out to participants at the speeches that we give. We are a CPA firm that specializes in entrepreneurs and realtors. We would like a flyer that looks crisp and clean, that integrates our logo and our company colors (shades of blue & gold). We would like the wording to be as laid out in the attached documents, but design is up to you. We would like a picture to go along with each point and are open to ideas. The flyer should be one page, preferably just the front.

Colors
3176b5
fee18a

Requirements
Must have
• Our logo and the wording supplied.
• A picture to go along with each topic.
Nice to have
• Images that pop, clean look, professional.
Should not have
• Look messy.

```html
<!DOCTYPE html>
<html lang="en">
<head>
<meta charset="utf-8">
<title>Nine Rung Ledger Remedy Seminar</title>
<link rel="stylesheet" href="https://fonts.googleapis.com/css2?family=Oswald:wght@500&family=PT+Sans:wght@400;700&family=PT+Serif:ital@1&display=swap">
<style>
  :root {
    --brand-blue: #3166b0;
    --brand-blue-deep: #2c5a9e;
    --brand-gold: #d4a62a;
    --ink: #3a3a3a;
    --paper: #ffffff;
    --paper-shade: #eeeeef;
    --rule: #2f5fa6;
  }
  * { margin: 0; padding: 0; box-sizing: border-box; }
  html, body { width: 1006px; height: 1200px; overflow: hidden; background: #f2f2f2; }
  .flyer {
    position: relative; width: 1006px; height: 1200px; overflow: hidden;
    background: radial-gradient(ellipse at 50% 70%, var(--paper) 0%, var(--paper-shade) 100%);
    font-family: "PT Sans", sans-serif; color: var(--ink);
  }
  .brand { position: absolute; left: 35px; top: 36px; z-index: 3; }
  .brand-name {
    font-family: "PT Sans", sans-serif; font-weight: 700; font-size: 46px;
    color: var(--brand-blue); line-height: 1; letter-spacing: -0.5px;
    display: flex; align-items: center; gap: 10px;
  }
  .brand-mark { width: 16px; height: 16px; background: var(--brand-gold); }
  .brand-tagline {
    font-family: "PT Serif", serif; font-style: italic; font-size: 15px;
    color: #1d1d1d; margin-top: 48px;
  }
  .header-art { position: absolute; left: 0; top: 0; width: 1006px; height: 525px; z-index: 1; }
  .seminar-title {
    position: absolute; left: 0; right: 0; top: 312px; text-align: center;
    font-family: "Oswald", sans-serif; font-weight: 500; font-size: 54px; line-height: 1.1;
    color: #fff; letter-spacing: -0.5px; z-index: 2;
  }
  .motto {
    position: absolute; top: 530px; left: 0; right: 0; z-index: 2;
    display: flex; align-items: center; gap: 18px;
    font-size: 22px; line-height: 30px; color: #222;
  }
  .motto::before, .motto::after { content: ""; height: 2px; background: var(--rule); flex: 1; }
  .motto::before { max-width: 155px; }
  .point { position: absolute; display: flex; gap: 20px; }
  .point-icon {
    flex: 0 0 70px; height: 70px; border-radius: 10px;
    background: linear-gradient(180deg, #3a6fb8, var(--brand-blue-deep));
    display: flex; align-items: center; justify-content: center;
    box-shadow: 0 2px 3px rgba(0,0,0,.25);
  }
  .point-icon svg { width: 38px; height: 38px; fill: #fff; }
  .point p { font-size: 17px; line-height: 22px; text-align: justify; color: var(--ink); margin-top: -3px; }
  .left { left: 30px; width: 440px; }
  .right { left: 508px; width: 455px; }
  .footer {
    position: absolute; left: 0; bottom: 0; width: 100%; height: 68px;
    background: var(--brand-blue-deep); color: #fff;
    display: flex; align-items: center; justify-content: center;
    font-weight: 700; font-size: 17.5px; letter-spacing: .2px;
  }
  .footer span { margin: 0 10px; }
</style>
</head>
<body>
<main class="flyer">
  <header>
    <div class="brand">
      <div class="brand-name"><span class="brand-mark"></span>Tallied Outcomes</div>
      <div class="brand-tagline">A Professional Accounting Corporation</div>
    </div>

    <svg class="header-art" viewBox="0 0 1006 525">
      <defs>
        <linearGradient id="officePhoto" x1="0" y1="0" x2="1" y2="1">
          <stop offset="0" stop-color="#f4f4f4"/>
          <stop offset=".5" stop-color="#c9c9cb"/>
          <stop offset="1" stop-color="#9d8a7c"/>
        </linearGradient>
        <linearGradient id="silhouettePhoto" x1="0" y1="0" x2="1" y2="0">
          <stop offset="0" stop-color="#1e1e1e"/>
          <stop offset=".5" stop-color="#3d3d3f"/>
          <stop offset="1" stop-color="#1a1a1a"/>
        </linearGradient>
        <linearGradient id="deskPhoto" x1="0" y1="0" x2="1" y2="1">
          <stop offset="0" stop-color="#8d99a8"/>
          <stop offset=".6" stop-color="#d8d8d8"/>
          <stop offset="1" stop-color="#f0f0f0"/>
        </linearGradient>
      </defs>
      <path role="img" aria-label="Photo of hands reviewing printed documents at an office desk"
            d="M420 178 Q700 60 1006 90 L1006 400 Q820 210 520 172 Z"
            fill="url(#officePhoto)"/>
      <path role="img" aria-label="Dark photo of business people in an office"
            d="M0 278 Q250 150 520 170 Q820 200 1006 398 Q960 470 820 502 Q680 528 560 512 Q400 485 300 420 Q160 300 0 290 Z"
            fill="url(#silhouettePhoto)"/>
      <path role="img" aria-label="Photo of a hand writing on tax forms beside a calculator"
            d="M0 290 Q160 300 300 420 Q325 440 345 448 Q200 460 0 442 Z"
            fill="url(#deskPhoto)"/>
    </svg>
    <h1 class="seminar-title">Nine Rung Ledger Remedy</h1>
  </header>

  <div class="motto">If they drive by with a machine gun you don’t have to stand up</div>

  <section>
    <div class="point left" style="top:613px">
      <div class="point-icon"><svg viewBox="0 0 24 24"><path d="M9 4h6a1 1 0 0 1 1 1v2h4a2 2 0 0 1 2 2v10a2 2 0 0 1-2 2H4a2 2 0 0 1-2-2V9a2 2 0 0 1 2-2h4V5a1 1 0 0 1 1-1zm1 3h4V6h-4zM2 12h20v1H2z"/></svg></div>
      <p>We will first show you how to eliminate much of your self-employment tax on your return by converting your business into an S Corporation. A business owner making over $120,000 per year can save about $12,000 per year by doing this.</p>
    </div>
    <div class="point left" style="top:801px">
      <div class="point-icon"><svg viewBox="0 0 24 24"><path d="M9 2h6l-2 4h-2zM10 7h4c4 2 7 6 7 10a5 5 0 0 1-5 5H8a5 5 0 0 1-5-5c0-4 3-8 7-10zm1 4v1.2c-1.2.3-2 1.1-2 2.1 0 1.3 1.2 1.8 2.6 2.1 1 .2 1.4.4 1.4.8s-.5.7-1.2.7c-.8 0-1.3-.3-1.5-.9l-1.4.5c.3 1 1.1 1.600 2.1 1.8V20h1.5v-1.2c1.2-.3 2-1.1 2-2.2 0-1.4-1.2-1.9-2.6-2.2-1-.2-1.4-.4-1.4-.8s.4-.6 1-.6c.7 0 1.1.3 1.3.8l1.4-.5c-.3-.9-1-1.4-1.7-1.6V11z"/></svg></div>
      <p>We will show you how to get tax free income from your corporation by renting you home to the corporation for the board meetings. Many of our clients are getting up to $21,000 in tax free income which could put $8,400 cash into your pocket.</p>
    </div>
    <div class="point left" style="top:973px">
      <div class="point-icon"><svg viewBox="0 0 24 24"><path d="M3 20h3v-4H3zm5 0h3v-7H8zm5 0h3v-9h-3zm5 0h3V8h-3zM3 13l6-5 4 3 6-6-2-1h6v6l-2-2-8 8-4-3-6 5z"/></svg></div>
      <p>We will show you the easiest way to track your expenses so that the only thing you will have to do to have rock solid books is to take a picture of the receipt and throw it away.&nbsp; It doesn’t get any better than that.</p>
    </div>

    <div class="point right" style="top:613px">
      <div class="point-icon"><svg viewBox="0 0 24 24"><path d="M6 2h12a2 2 0 0 1 2 2v16a2 2 0 0 1-2 2H6a2 2 0 0 1-2-2V4a2 2 0 0 1 2-2zm1 3v4h10V5zm0 7v2h2v-2zm4 0v2h2v-2zm4 0v2h2v-2zm-8 4v2h2v-2zm4 0v2h2v-2zm4 0v2h2v-2z"/></svg></div>
      <p>Next, we show you the importance of tax planning and why it is critical to meet with your CPA before the end of the year and not just when you do your tax preparation.</p>
    </div>
    <div class="point right" style="top:727px">
      <div class="point-icon"><svg viewBox="0 0 24 24"><path d="M12 2l10 9h-3v10H5V11H2zm-3 10a1.5 1.5 0 1 0 0 3 1.5 1.5 0 0 0 0-3zm6 0a1.5 1.5 0 1 0 0 3 1.5 1.5 0 0 0 0-3zm-7.5 4v4h3v-4zm6 0v4h3v-4z"/></svg></div>
      <p>We will show you how to hire your children and get $7,500 per child tax free. This will save you $3,000 per child in income tax reduction.</p>
    </div>
    <div class="point right" style="top:841px">
      <div class="point-icon"><svg viewBox="0 0 24 24"><path d="M12 4l11 5-11 5L1 9zm-6 7.5l6 2.7 6-2.7V16c0 1.7-2.7 3-6 3s-6-1.3-6-3zM20 10l1 .5V17h-1z"/></svg></div>
      <p>We will discuss how to make your child’s college education tax deductible. With college cost spiraling out of control this is a biggie. Most of our clients have a savings of about $12,000 per year of college.</p>
    </div>
    <div class="point right" style="top:972px">
      <div class="point-icon"><svg viewBox="0 0 24 24"><path d="M12 2l10 5v2H2V7zM4 10h3v8H4zm6.5 0h3v8h-3zM17 10h3v8h-3zM2 19h20v3H2z"/></svg></div>
      <p>Our grand finale is to show you how to use, not one, but two corporations to get a several hundred thousand dollar tax deferral, get an interest free loan from the government and use that money to grow your business and your wealth.</p>
    </div>
  </section>

  <footer class="footer">
    2870 E. Grove Ave, Ste. B, Lodi, CA 95240<span>|</span>209-555-0147<span>|</span>www.talliedoutcomescpa.com
  </footer>
</main>
</body>
</html>
```